Four in One (Flexible infographic for Content Management Industry)

See attachment.
A graphic depicting 4 products, where each can stand on its own and each can be combined with others, but where, if all are taken together, the best result is achieved (the "super product").
Intended use is web. See attached file as an example.
The most basic idea is as the attached diagram shows, where 4 rectangles are arranged in a quadrangle, with a middle rectangle in the center representing the combined 4 products. This concept is fine except it is a bit too obvious as it stands. We are looking for either a variation of this or another concept.
The audience is technical + professional + enterprise - NOT consumers. Hence the design should be conservative in nature.
We are aware of tools like as Canva or Pictogram where such graphics are available, but we are looking for something with a bit more imagination and flexibility.
This graphic should be targeted to web sites and be delivered with vector-based (SVG) graphics.

```html
<!DOCTYPE html>
<html lang="en">
<head>
<meta charset="utf-8">
<title>Four in One – Super Product</title>
<link href="https://fonts.googleapis.com/css2?family=Barlow:wght@500;600;800&family=Nunito+Sans:wght@400;500&display=swap" rel="stylesheet">
<style>
  :root{
    --green:#3ccb8f;
    --purple:#8a4fb6;
    --blue:#0b67b8;
    --cyan:#09a6cf;
    --ink:#1f2430;
    --indigo:#2f2b8e;
    --teal:#7fcfbf;
    --deep-blue:#0870c2;
    --paper:#ffffff;
  }
  *{box-sizing:border-box;margin:0;padding:0}
  html,body{width:1200px;height:928px;overflow:hidden}
  body{
    position:relative;
    background:linear-gradient(100deg,#ffffff 0%,#f7f7f8 55%,#dedfe1 100%);
    font-family:"Nunito Sans",sans-serif;color:var(--ink);
  }
  .frame{
    position:absolute;left:161px;top:132px;width:880px;height:664px;
    background:linear-gradient(135deg,var(--indigo) 0%,#3d4a9c 30%,var(--teal) 55%,#4aa6c4 80%,var(--deep-blue) 100%);
  }
  .card{
    position:absolute;left:178px;top:149px;width:846px;height:630px;
    background:var(--paper);border-radius:30px;overflow:hidden;
  }
  .card .shade-br{position:absolute;left:423px;top:315px;width:423px;height:315px;background:#f5fafd}
  .card .shade-tr{position:absolute;left:520px;top:-120px;width:520px;height:320px;border-radius:50%;
    background:radial-gradient(ellipse at 70% 30%,rgba(205,236,221,.35),rgba(255,255,255,0) 70%)}
  .divider{position:absolute}
  .divider.v-top{left:600px;top:149px;width:2px;height:315px;background:linear-gradient(#1a9a55,#3ccb8f)}
  .divider.v-bottom{left:600px;top:464px;width:2px;height:315px;background:linear-gradient(var(--blue),var(--cyan))}
  .divider.h-left{left:178px;top:463px;width:423px;height:2px;background:linear-gradient(90deg,var(--indigo),var(--blue))}
  .divider.h-right{left:601px;top:463px;width:423px;height:2px;background:linear-gradient(90deg,#b35fe0,var(--purple) 50%,var(--blue))}

  .quadrant{position:absolute;width:360px;z-index:2}
  .quadrant.left{left:211px;text-align:left}
  .quadrant.right{right:208px;text-align:right}
  .quadrant h2{
    font-family:"Barlow",sans-serif;font-weight:800;font-size:24px;line-height:29px;letter-spacing:.2px;
  }
  .quadrant .rule{height:2px;width:185px;margin:8px 0 10px;opacity:.5}
  .quadrant.right .rule{margin-left:auto}
  .quadrant p{font-size:14px;line-height:17.4px;color:#2a2e38;white-space:nowrap}
  .features{list-style:none;margin-top:19px}
  .features li{
    font-family:"Barlow",sans-serif;font-weight:500;font-size:14.5px;height:27px;line-height:21px;
    display:flex;align-items:center;gap:8px;position:relative;letter-spacing:.2px;white-space:nowrap;
  }
  .quadrant.right .features li{justify-content:flex-end}
  .features li::after{content:"";position:absolute;bottom:1px;width:165px;height:1px;background:linear-gradient(90deg,rgba(0,0,0,0),rgba(0,0,0,.12),rgba(0,0,0,0))}
  .quadrant.left .features li::after{left:12px}
  .quadrant.right .features li::after{right:12px}
  .features svg{width:15px;height:15px;flex:none}
  .features .small{font-size:13px}

  .doc h2,.doc .features svg{color:var(--green)} .doc .rule{background:linear-gradient(90deg,var(--green),transparent)}
  .sec h2,.sec .features svg{color:var(--purple)} .sec .rule{background:linear-gradient(270deg,var(--purple),transparent)}
  .erp h2,.erp .features svg{color:var(--blue)} .erp .rule{background:linear-gradient(90deg,transparent,var(--blue) 40%,transparent)}
  .dig h2,.dig .features svg{color:var(--cyan)} .dig .rule{background:linear-gradient(270deg,transparent,var(--cyan) 40%,transparent)}

  .doc{top:186px} .sec{top:184px} .erp{top:506px} .dig{top:506px}
  .sec .features{margin-top:18px}

  .hub{position:absolute;left:446px;top:309px;width:310px;height:310px;z-index:1}
  .hub-title{
    position:absolute;left:446px;top:443px;width:310px;text-align:center;z-index:3;
    font-family:"Barlow",sans-serif;font-weight:800;font-size:23px;color:#fff;letter-spacing:.3px;
  }
</style>
</head>
<body>
<svg width="0" height="0" style="position:absolute" aria-hidden="true">
  <symbol id="tick" viewBox="0 0 20 20">
    <path d="M17.2 8.6A7.4 7.4 0 1 1 13.4 3.6" fill="none" stroke="currentColor" stroke-width="1.7" stroke-linecap="round"/>
    <path d="M6.6 9.8l3 3 7.6-8.2" fill="none" stroke="currentColor" stroke-width="1.7" stroke-linecap="round" stroke-linejoin="round"/>
  </symbol>
</svg>

<div class="frame"></div>
<div class="card">
  <div class="shade-br"></div>
  <div class="shade-tr"></div>
</div>
<div class="divider v-top"></div>
<div class="divider v-bottom"></div>
<div class="divider h-left"></div>
<div class="divider h-right"></div>

<svg class="hub" viewBox="0 0 310 310">
  <defs>
    <linearGradient id="coreFill" x1="0" y1="0" x2="0" y2="1">
      <stop offset="0" stop-color="#4f95e6"/>
      <stop offset=".5" stop-color="#9a6bf2"/>
      <stop offset="1" stop-color="#ee4f96"/>
    </linearGradient>
  </defs>
  <circle cx="155" cy="155" r="152" fill="#f0f0f2"/>
  <circle cx="155" cy="155" r="139" fill="#fff"/>
  <g fill="none" stroke-width="12">
    <circle cx="155" cy="155" r="133" stroke="#1a9aa8" stroke-dasharray="209 627"/>
    <circle cx="155" cy="155" r="133" stroke="#1f5fb0" stroke-dasharray="209 627" transform="rotate(90 155 155)"/>
    <circle cx="155" cy="155" r="133" stroke="#39b57c" stroke-dasharray="209 627" transform="rotate(180 155 155)"/>
    <circle cx="155" cy="155" r="133" stroke="#7b52c0" stroke-dasharray="209 627" transform="rotate(270 155 155)"/>
  </g>
  <circle cx="155" cy="155" r="122" fill="#fff"/>
  <circle cx="155" cy="155" r="118" fill="none" stroke="#3ccb8f" stroke-width="2" stroke-dasharray="185 556" transform="rotate(180 155 155)"/>
  <circle cx="155" cy="155" r="118" fill="none" stroke="#a45de0" stroke-width="2" stroke-dasharray="185 556" transform="rotate(270 155 155)"/>
  <circle cx="155" cy="155" r="118" fill="none" stroke="#0b67b8" stroke-width="2" stroke-dasharray="185 556" transform="rotate(90 155 155)"/>
  <circle cx="155" cy="155" r="118" fill="none" stroke="#09a6cf" stroke-width="2" stroke-dasharray="185 556"/>
  <circle cx="155" cy="155" r="112" fill="url(#coreFill)" role="img" aria-label="Circuit board pattern in blue, violet and pink representing the combined product"/>

  <g>
    <circle cx="55" cy="54" r="38" fill="#fff"/>
    <circle cx="55" cy="54" r="30" fill="#3ccb8f"/>
    <path d="M44 44h14v8h-6v18h-8z" fill="none" stroke="#fff" stroke-width="2" stroke-linejoin="round"/>
    <circle cx="61" cy="43" r="6" fill="none" stroke="#fff" stroke-width="2"/>
    <path d="M58 43l2 2 4-4" fill="none" stroke="#fff" stroke-width="1.8"/>
  </g>
  <g>
    <circle cx="252" cy="57" r="38" fill="#fff"/>
    <circle cx="252" cy="57" r="30" fill="#a45de0"/>
    <path d="M240 66a7 7 0 0 1 1-14 10 10 0 0 1 19-2 7 7 0 0 1 3 16" fill="none" stroke="#fff" stroke-width="2" stroke-linecap="round"/>
    <path d="M252 58l7 3v5c0 4-3 7-7 8-4-1-7-4-7-8v-5z" fill="none" stroke="#fff" stroke-width="2" stroke-linejoin="round"/>
    <path d="M249 66l2 2 4-4" fill="none" stroke="#fff" stroke-width="1.8"/>
  </g>
  <g>
    <circle cx="55" cy="231" r="38" fill="#fff"/>
    <circle cx="55" cy="231" r="30" fill="#0b67b8"/>
    <circle cx="55" cy="231" r="5" fill="none" stroke="#fff" stroke-width="2"/>
    <circle cx="55" cy="231" r="10" fill="none" stroke="#fff" stroke-width="2" stroke-dasharray="4 3"/>
    <path d="M39 226a17 17 0 0 1 28-9M71 236a17 17 0 0 1-28 9" fill="none" stroke="#fff" stroke-width="2" stroke-linecap="round"/>
  </g>
  <g>
    <circle cx="252" cy="233" r="38" fill="#fff"/>
    <circle cx="252" cy="233" r="30" fill="#0ba0b8"/>
    <rect x="239" y="221" width="24" height="22" rx="3" fill="none" stroke="#fff" stroke-width="2"/>
    <path d="M239 227h24M243 233h6M243 238h4" stroke="#fff" stroke-width="2"/>
    <circle cx="259" cy="240" r="4" fill="#0ba0b8" stroke="#fff" stroke-width="2"/>
    <path d="M262 243l3 3" stroke="#fff" stroke-width="2" stroke-linecap="round"/>
  </g>
</svg>
<div class="hub-title">SUPER PRODUCT</div>

<section class="quadrant left doc">
  <h2>DOCUMENT<br>MANAGEMENT</h2>
  <div class="rule"></div>
  <p>Streamline document organization, access, and<br>collaboration with easier file storage and sharing,<br>leading to more effecient workflows.</p>
  <ul class="features">
    <li><svg><use href="#tick"/></svg>Centralized Document Control</li>
    <li class="small"><svg><use href="#tick"/></svg>Collaborative Workspace Integration</li>
    <li><svg><use href="#tick"/></svg>Automated Compliance Tracking</li>
    <li><svg><use href="#tick"/></svg>Check 4</li>
  </ul>
</section>

<section class="quadrant right sec">
  <h2>SECURITY &amp;<br>COMPLIANCE</h2>
  <div class="rule"></div>
  <p>Benefit from tailored cloud solutions, secure data<br>storage, and expert disaster recovery planning for<br>reliable and scalable IT operations.</p>
  <ul class="features">
    <li>Custom cloud Solutions<svg><use href="#tick"/></svg></li>
    <li>Secure Data Storage<svg><use href="#tick"/></svg></li>
    <li>Expert Disaster Recovery<svg><use href="#tick"/></svg></li>
    <li>Check 4<svg><use href="#tick"/></svg></li>
  </ul>
</section>

<section class="quadrant left erp">
  <h2>ENTERPRISE<br>RESOURCE PLANNING</h2>
  <div class="rule"></div>
  <p>Simplify management across finance,<br>sales, and operations, enabling better<br>decision-making and improved productivity.</p>
  <ul class="features">
    <li><svg><use href="#tick"/></svg>Integrated Business Processes</li>
    <li><svg><use href="#tick"/></svg>Enhanced Decision-Making</li>
    <li><svg><use href="#tick"/></svg>Productivity Improvement</li>
    <li><svg><use href="#tick"/></svg>Check 4</li>
  </ul>
</section>

<section class="quadrant right dig">
  <h2>DIGITAL<br>TRANSFORMATION</h2>
  <div class="rule"></div>
  <p>Turn scanned documents into easily<br>searchable digital archives, boosting effeciency<br>and accessibility.</p>
  <ul class="features">
    <li>Instant searchable Archives with OCR<svg><use href="#tick"/></svg></li>
    <li>Automated Document Classification<svg><use href="#tick"/></svg></li>
    <li>TeamVault and Cloud Blob Ready<svg><use href="#tick"/></svg></li>
    <li>Check 4<svg><use href="#tick"/></svg></li>
  </ul>
</section>
</body>
</html>
```